Modify mobile web Photoshop design to make them look great

We need to choose and refine the stock image to look great on 5 mobile web pages: 1) Hourglass image on home screen, 2) Sofa image on registration screen, 3) Loveseat image on login screen, 4) Lamp for reminder screen, and 5) Bed for ratings / score screen. Sample photos denote what customer wants, but they are just downloaded from Vantry, and is not purchased stock photos. Designers need to show that the updated photos used are properly purchased from stock photo source. Photoshop files for all 5 mobile web pages are provided. Artists are requested to edit and submit the 5 photoshop files and make them look as good as possible with the constraints above. No change is needed on the layout or anything beside the 5 stock images, but subtle refinements are OK if you believe it would improve the overall design without affecting the art direction.

Target Market(s)

Travel, Lifestyle

Industry/Entity Type

Hospitality

Font styles to use
Sans Serif

Requirements
Must have
• Stock photos must be properly licensed, artists must put updated stock photos back into supplied photoshop source files, updated look and feel should have the same general art direction, images must be hourglass, sofa, loveseat, lamp and bed
Nice to have
• Minor and very subtle touchup of other elements without affecting any design work of the layout such as color scheme
Should not have
• Should not affect art direction, identity and color of all design and layout elements, should not use stock image other than the types specified (hourglass, sofa, loveseat, lamp and bed), should not use images not licensed from stock photo sites

```html
<!DOCTYPE html>
<html lang="en">
<head>
<meta charset="utf-8">
<title>lumora.co — Hotel Booking Home</title>
<link rel="stylesheet" href="https://fonts.googleapis.com/css2?family=Nunito:wght@600;700;800&family=Oswald:wght@600;700&display=swap">
<style>
  :root {
    --bg: #e9e9ea;
    --white: #ffffff;
    --ink: #141414;
    --brand: #8b3aa3;
    --panel-orange: #d4894f;
    --card-peach: #e8bfa0;
    --search-gray: #b9b9b9;
    --search-divider: #a3a3a3;
    --leisure: #b184dc;
    --food: #12a099;
    --beauty: #a1137f;
    --life: #f0b789;
    --badge-black: #111111;
    --login-gray: #e6e6e6;
  }
  * { box-sizing: border-box; margin: 0; padding: 0; }
  html, body { width: 1200px; height: 1200px; overflow: hidden; background: var(--bg); }
  body { display: flex; align-items: center; justify-content: center; font-family: "Nunito", sans-serif; }

  .screen {
    width: 640px; height: 1136px; background: var(--white);
    display: flex; flex-direction: column; overflow: hidden;
    box-shadow: 0 10px 40px rgba(0,0,0,0.12);
  }

  .site-header {
    height: 76px; display: flex; align-items: center; justify-content: space-between;
    padding: 0 28px; background: var(--white);
  }
  .brand-name { font-weight: 800; font-size: 40px; color: var(--brand); letter-spacing: -0.5px; }
  .menu-toggle { width: 34px; height: 24px; display: flex; flex-direction: column; justify-content: space-between; }
  .menu-toggle span { height: 3px; background: #555; border-radius: 2px; }

  .hero-photo {
    height: 372px;
    background: radial-gradient(ellipse at 62% 40%, #e9d3b4 0%, #c8a070 35%, #8a5f33 75%, #5a3b1e 100%);
  }

  .booking-panel { height: 428px; background: var(--panel-orange); padding: 22px 26px 26px; }
  .booking-card {
    height: 100%; background: var(--card-peach); border-radius: 10px;
    display: flex; flex-direction: column; justify-content: flex-end;
    position: relative;
  }
  .booking-title { position: absolute; left: 0; right: 0; top: 130px; text-align: center; color: var(--ink); font-family: "Oswald", sans-serif; }
  .booking-title .title-main { display: block; font-size: 86px; font-weight: 700; line-height: 0.9; letter-spacing: -1px; }
  .booking-title .title-sub { display: block; font-size: 30px; font-weight: 600; line-height: 1.1; margin-left: 90px; }

  .search-bar {
    height: 64px; margin: 0 22px 22px; background: var(--search-gray); border-radius: 10px;
    display: flex; align-items: stretch; font-size: 23px; font-weight: 600; color: #2a2a2a;
  }
  .search-input { flex: 1; display: flex; align-items: center; padding-left: 24px; }
  .search-region { width: 150px; display: flex; align-items: center; justify-content: center; gap: 8px; border-left: 2px solid var(--search-divider); }
  .search-button { width: 72px; display: flex; align-items: center; justify-content: center; border-left: 2px solid var(--search-divider); }

  .category-row { height: 132px; display: flex; }
  .category-tile {
    flex: 1; display: flex; flex-direction: column; align-items: center; justify-content: center; gap: 10px;
    color: var(--white); font-size: 17px; font-weight: 800; letter-spacing: 1px; text-transform: uppercase;
  }
  .tile-leisure { background: var(--leisure); }
  .tile-food { background: var(--food); }
  .tile-beauty { background: var(--beauty); }
  .tile-life { background: var(--life); }

  .site-footer { flex: 1; display: flex; align-items: center; justify-content: space-between; padding: 0 26px; }
  .store-badges { display: flex; gap: 14px; }
  .store-badge { width: 150px; height: 50px; background: var(--badge-black); border-radius: 8px; }
  .login-button {
    display: flex; align-items: center; gap: 10px; background: var(--login-gray); border-radius: 8px;
    padding: 12px 22px; font-size: 20px; font-weight: 800; color: var(--ink); letter-spacing: 0.5px;
  }
</style>
</head>
<body>
  <main class="screen">
    <header class="site-header">
      <div class="brand-name">lumora.co</div>
      <div class="menu-toggle" aria-label="Menu"><span></span><span></span><span></span></div>
    </header>

    <div class="hero-photo" role="img" aria-label="Photo of an hourglass with sand on a warm wooden table"></div>

    <section class="booking-panel">
      <div class="booking-card">
        <h1 class="booking-title">
          <span class="title-main">Hotel</span>
          <span class="title-sub">Booking Now</span>
        </h1>
        <form class="search-bar">
          <div class="search-input">Search Hotel</div>
          <div class="search-region">Region
            <svg width="12" height="8" viewBox="0 0 12 8"><path d="M0 0h12L6 8z" fill="#2a2a2a"/></svg>
          </div>
          <div class="search-button">
            <svg width="28" height="28" viewBox="0 0 28 28" fill="none" stroke="#1a1a1a" stroke-width="3">
              <circle cx="11" cy="11" r="8"/><path d="M17 17l8 8" stroke-linecap="round"/>
            </svg>
          </div>
        </form>
      </div>
    </section>

    <nav class="category-row">
      <div class="category-tile tile-leisure">
        <svg width="40" height="36" viewBox="0 0 40 36" fill="none" stroke="#fff" stroke-width="3" stroke-linecap="round">
          <circle cx="14" cy="8" r="4" fill="#fff" stroke="none"/><path d="M8 30l10-14 8 6 8-4M4 32h32"/>
        </svg>
        Leisure
      </div>
      <div class="category-tile tile-food">
        <svg width="44" height="36" viewBox="0 0 44 36" fill="none" stroke="#fff" stroke-width="3" stroke-linecap="round">
          <path d="M6 26a16 16 0 0 1 32 0z"/><path d="M2 30h40"/><circle cx="22" cy="7" r="2.5" fill="#fff"/>
        </svg>
        Food
      </div>
      <div class="category-tile tile-beauty">
        <svg width="40" height="36" viewBox="0 0 40 36" fill="none" stroke="#fff" stroke-width="3" stroke-linecap="round">
          <circle cx="20" cy="14" r="8"/><path d="M10 30h20M20 22v8M6 8c2-3 4-3 6 0M28 8c2-3 4-3 6 0"/>
        </svg>
        Beauty
      </div>
      <div class="category-tile tile-life">
        <svg width="40" height="36" viewBox="0 0 40 36" fill="none" stroke="#fff" stroke-width="3" stroke-linecap="round">
          <path d="M5 16h30a15 15 0 0 1-30 0z" fill="#fff"/><path d="M14 12c0-5 4-8 8-8M24 12l6-8"/>
        </svg>
        Life
      </div>
    </nav>

    <footer class="site-footer">
      <div class="store-badges">
        <div class="store-badge" aria-label="App download badge"></div>
        <div class="store-badge" aria-label="App download badge"></div>
      </div>
      <a class="login-button">
        <svg width="18" height="22" viewBox="0 0 18 22">
          <path d="M4 9V6a5 5 0 0 1 10 0v3" fill="none" stroke="#141414" stroke-width="3"/>
          <rect x="1" y="9" width="16" height="12" rx="2" fill="#141414"/>
        </svg>
        LOGIN
      </a>
    </footer>
  </main>
</body>
</html>
```